Marrowind Booking Engine Marketing Site

Hi,
I’m currently in the process of putting together a web application with the intention of providing small resorts/B&Bs/small hotels the ability to allow their customers to book online.
I’m looking to have a design created for a marketing site, to give potential customers additional information about my booking engine, as well as to help drive sign-ups. A lot of the competition out there appears outdated, so I would like something that is more modern and up to date.
I am looking for just the design (i’m a web developer, but I lack the creative skills for a good marketing site)
For some more background, I will be targeting business owners of smaller resorts and Bed & Breakfasts. These are typically family owned small businesses that may only have a 10 room setup. These businesses will also typically have additional amenities that they will have to rent out or sell to their clients ( ex. Spa, fruit basket, water sport rentals). My software will provide them with the ability to sell their amenities as well.
I’m open to different designs, but my main thing is I want it to look modern, and I want it to have several callouts to sign up for my product.
I am looking to have the homepage created, 1 interior page, and a style guide created (to show form fields, H1’s, etc.).
I had a logo created a couple months ago that will be included with this project brief.
If you need any additional information feel free to reach out to me.

Target Market(s)

This site will be targeted small business owners who are running small resorts, Bed and Breakfasts, or any business that provides rooms for their clients.

Industry/Entity Type

Saas

Number of Pages Required

2 page

Font styles to use
Sans Serif

Colors

Designer to choose colors to be used in the design.

Requirements
Must have
• A modern feel, with several CTA's that will drive to the registration page on the homepage. on the internal page, I mostly just need the page layout, I will reuse that page layout. and a style guide if at all possible (include colors, form fields, H1's, etc.)
Nice to have
• maybe a hero image at the top with buttons over the top? again i'm pretty open to most anything.
Should not have
• I like images, but I don't want the page overrun with images. A good balance.

```html
<!DOCTYPE html>
<html lang="en">
<head>
<meta charset="utf-8">
<title>Marrowind Booking Engine</title>
<link rel="stylesheet" href="https://fonts.googleapis.com/css2?family=Roboto:wght@400;500;700&display=swap">
<style>
:root{
  --page:#f1f4f5;
  --white:#ffffff;
  --ink:#1f2530;
  --muted:#8f949a;
  --cyan:#3fc8e4;
  --blue-a:#5aa6e2;
  --blue-b:#43c0e0;
  --green:#5bbf00;
  --line:#c9cdd2;
  --bar:#efefef;
}
*{margin:0;padding:0;box-sizing:border-box}
html,body{width:1200px;height:2222px;overflow:hidden}
body{background:var(--page);font-family:"Roboto",Arial,sans-serif;color:var(--ink);position:relative}
.abs{position:absolute}

.section-title{font-size:30px;font-weight:400;color:var(--ink);line-height:1}
.title-rule{height:1.5px;width:76px;background:var(--cyan)}
.section-sub{font-size:15px;color:var(--muted)}

.feature-card{background:var(--white);width:456px;height:171px;box-shadow:0 6px 18px rgba(0,0,0,.04)}
.feature-card svg{position:absolute;left:41px;top:38px}
.feature-card h3{position:absolute;left:134px;top:38px;font-size:21px;font-weight:400}
.feature-card p{position:absolute;left:135px;top:73px;width:290px;font-size:14px;line-height:21px;color:var(--muted)}

.promo-band{left:0;top:658px;width:1200px;height:472px}
.promo-photo{left:0;top:723px;width:316px;height:332px;border-radius:0 40px 40px 0;background:linear-gradient(135deg,#e8dccd,#c6cfd6 60%,#7cc96d)}
.promo-title{left:455px;top:752px;width:480px;font-size:28px;font-weight:500;line-height:37px;color:var(--white)}
.promo-text{left:455px;top:845px;width:520px;font-size:15.5px;line-height:26px;color:var(--white)}
.btn{background:var(--green);color:var(--white);font-size:13.5px;text-align:center;border-radius:14px;letter-spacing:.3px}

.news-card{background:var(--white);width:457px;height:391px;top:1325px;overflow:hidden}
.news-photo{position:absolute;left:0;top:0;width:457px;height:211px}
.date-badge{position:absolute;left:-68px;top:-68px;width:136px;height:136px;border-radius:50%;background:var(--cyan);color:var(--white)}
.date-badge b{position:absolute;left:84px;top:78px;font-size:22px;font-weight:400}
.date-badge span{position:absolute;left:86px;top:104px;font-size:11px}
.news-card h3{position:absolute;left:22px;top:235px;font-size:21px;font-weight:400}
.news-card p{position:absolute;left:22px;top:267px;width:402px;font-size:14px;line-height:21px;color:var(--muted)}
.read-more{position:absolute;left:22px;top:341px;font-size:13.5px;color:var(--cyan);letter-spacing:.5px}

.footer{left:0;top:1822px;width:1200px;height:322px;background:var(--white)}
.brand{left:134px;top:1885px;display:flex;align-items:center;gap:8px}
.brand-dot{width:26px;height:26px;border-radius:50%;background:#2a7bbf}
.brand-name{font-size:21px;color:#1f5f9e;font-weight:500;letter-spacing:.5px}
.footer-text{font-size:14px;line-height:21px;color:var(--muted)}
.social{left:134px;top:2009px;display:flex;gap:17px}
.social i{width:10px;height:10px;border-radius:50%;background:#8f949a;display:block}
.contact-row{left:452px;display:flex;gap:12px;font-size:14px;line-height:19px;color:var(--muted)}
.field{border:1px solid var(--line);background:var(--white);font-size:12.5px;color:var(--muted);padding:8px 16px}

.bottom-bar{left:0;top:2144px;width:1200px;height:78px;background:var(--bar)}
.copyright{left:134px;top:2175px;font-size:13.5px;color:var(--muted)}
.nav{top:2176px;font-size:13px;color:#6c7177;letter-spacing:.3px}
</style>
</head>
<body>

<h1 class="abs section-title" style="left:134px;top:60px">Additional Features</h1>
<div class="abs title-rule" style="left:134px;top:98px"></div>
<p class="abs section-sub" style="left:134px;top:113px">Lorem ipsum dolor sit amet, consectetur adipiscing elit</p>

<svg width="0" height="0" class="abs"><defs>
<g id="team-icon" fill="none" stroke="#3fc8e4" stroke-width="2">
  <circle cx="27" cy="28" r="18"/>
  <circle cx="27" cy="6" r="4" fill="#fff"/><path d="M20 18a7 6 0 0 1 14 0z" fill="#fff"/>
  <circle cx="6" cy="27" r="4" fill="#fff"/><path d="M-1 39a7 6 0 0 1 14 0z" fill="#fff"/>
  <circle cx="48" cy="27" r="4" fill="#fff"/><path d="M41 39a7 6 0 0 1 14 0z" fill="#fff"/>
  <circle cx="27" cy="44" r="4" fill="#fff"/><path d="M20 56a7 6 0 0 1 14 0z" fill="#fff"/>
</g></defs></svg>

<div class="abs feature-card" style="left:134px;top:193px">
  <svg width="58" height="58" viewBox="-2 0 58 58"><use href="#team-icon"/></svg>
  <h3>Multi-User capabilities</h3>
  <p>Lorem ipsum dolor sit amet, consectetur adipiscing elit, sed do eiusmod tempor incididunt ut labore</p>
</div>
<div class="abs feature-card" style="left:608px;top:193px">
  <svg width="58" height="58" viewBox="-2 0 58 58"><use href="#team-icon"/></svg>
  <h3>Multi-Property capabilities</h3>
  <p>Lorem ipsum dolor sit amet, consectetur adipiscing elit, sed do eiusmod tempor incididunt ut labore</p>
</div>
<div class="abs feature-card" style="left:134px;top:381px">
  <svg width="58" height="58" viewBox="-2 0 58 58"><use href="#team-icon"/></svg>
  <h3>Rates Management</h3>
  <p>Lorem ipsum dolor sit amet, consectetur adipiscing elit, sed do eiusmod tempor incididunt ut labore</p>
</div>
<div class="abs feature-card" style="left:608px;top:381px">
  <svg width="58" height="58" viewBox="-2 0 58 58"><use href="#team-icon"/></svg>
  <h3>Integrated Analytics Tracking</h3>
  <p>Lorem ipsum dolor sit amet, consectetur adipiscing elit, sed do eiusmod tempor incididunt ut labore</p>
</div>

<svg class="abs promo-band" viewBox="0 0 1200 472" preserveAspectRatio="none">
  <defs><linearGradient id="promo-fill" x1="0" y1="0" x2="1" y2="1">
    <stop offset="0" stop-color="#48bde2"/><stop offset=".55" stop-color="#5aaae3"/><stop offset="1" stop-color="#42c1df"/>
  </linearGradient></defs>
  <path d="M0 0H1200V385C900 430 600 465 380 468C200 470 80 460 0 449Z" fill="url(#promo-fill)"/>
  <path d="M350 0L470 360L1200 40V0Z" fill="#ffffff" opacity=".05"/>
</svg>
<div class="abs promo-photo" role="img" aria-label="Photo of a hand holding out a house key on a green house-shaped keyring"></div>
<h2 class="abs promo-title">Lorem Ipsum Dolor Set Amet Adipiscing</h2>
<p class="abs promo-text">Lorem ipsum dolor sit amet, consectetur adipiscing elit, sed do eiusmod tempor incididunt ut labore et dolore magna aliqua. Ut enim ad minim veniam, quis nostrud exercitation ullamco laboris enim ad minim veniam, quis exercitation ullamco.</p>
<div class="abs btn" style="left:455px;top:972px;width:176px;height:27px;line-height:27px">SIGN UP</div>

<h2 class="abs section-title" style="right:134px;top:1191px">News and Updates</h2>
<div class="abs title-rule" style="right:134px;top:1230px"></div>
<p class="abs section-sub" style="right:134px;top:1244px">Lorem ipsum dolor sit amet, consectetur adipiscing elit</p>

<article class="abs news-card" style="left:134px">
  <div class="news-photo" role="img" aria-label="Photo of a city skyline and bridge lit up at dusk over the water" style="background:linear-gradient(180deg,#8a74c9 0%,#d17aa8 45%,#3a2b44 70%,#5b6fa8 100%)"></div>
  <div class="date-badge"><b>01</b><span>JAN</span></div>
  <h3>Lorem ipsum dolor</h3>
  <p>Lorem ipsum dolor sit amet, con sectet iscing elit, sed do eiusm od tetmpor ididunt ut labore et dolore magna aliqua. Sed ut perspiciatis unde omnis iste natus error sit voluptatem</p>
  <div class="read-more">READ MORE &nbsp;&#8250;</div>
</article>
<article class="abs news-card" style="left:608px">
  <div class="news-photo" role="img" aria-label="Photo of a woman looking at her phone on a city street" style="background:linear-gradient(90deg,#9fb3c7 0%,#c9b7b0 45%,#d95a7a 65%,#a9bccd 100%)"></div>
  <div class="date-badge"><b>07</b><span>JAN</span></div>
  <h3>Lorem ipsum dolor</h3>
  <p>Lorem ipsum dolor sit amet, con sectet iscing elit, sed do eiusm od tetmpor ididunt ut labore et dolore magna aliqua. Sed ut perspiciatis unde omnis iste natus error sit voluptatem</p>
  <div class="read-more">READ MORE &nbsp;&#8250;</div>
</article>

<footer class="abs footer"></footer>
<div class="abs brand"><span class="brand-dot"></span><span class="brand-name">MARROWIND</span></div>
<p class="abs footer-text" style="left:134px;top:1932px;width:270px">Lorem ipsum dolor sit amet, consectetur adipiscing elit, sed do eiusmod tempor incididunt ut labore</p>
<div class="abs social"><i></i><i></i><i></i><i></i></div>

<div class="abs contact-row" style="top:1880px">
  <svg width="12" height="16" viewBox="0 0 12 16"><path d="M6 0a6 6 0 0 1 6 6c0 4-6 10-6 10S0 10 0 6a6 6 0 0 1 6-6z" fill="#5bbf00"/><circle cx="6" cy="6" r="2.2" fill="#fff"/></svg>
  <span style="width:215px">Suite 4, Harbour Court, Elmsby, EL4 2RT.</span>
</div>
<div class="abs contact-row" style="top:1940px">
  <svg width="14" height="12" viewBox="0 0 14 12" style="margin-top:4px"><rect width="14" height="10" rx="1" fill="#5bbf00"/><path d="M1 1l6 5 6-5" stroke="#fff" fill="none"/></svg>
  <span>info@example.com</span>
</div>
<div class="abs contact-row" style="top:1989px">
  <svg width="13" height="13" viewBox="0 0 13 13" style="margin-top:3px"><path d="M3 0l2 3-1.5 1.5a8 8 0 0 0 5 5L10 8l3 2-1.5 3C6 13 0 7 0 1.5z" fill="#5bbf00"/></svg>
  <span>+(12)123 - 456 - 7890</span>
</div>

<div class="abs field" style="left:688px;top:1883px;width:182px;height:32px">Your Name</div>
<div class="abs field" style="left:882px;top:1883px;width:184px;height:32px">Your Email</div>
<div class="abs field" style="left:688px;top:1927px;width:378px;height:32px">Subject</div>
<div class="abs field" style="left:688px;top:1972px;width:378px;height:79px">Mesage</div>
<div class="abs btn" style="left:789px;top:2070px;width:176px;height:26px;line-height:26px">SUBMIT</div>

<div class="abs bottom-bar"></div>
<p class="abs copyright">©2018 All Rights Reserved</p>
<span class="abs nav" style="left:584px">HOME</span>
<span class="abs nav" style="left:665px">HOW IT WORKS</span>
<span class="abs nav" style="left:801px">ABOUT</span>
<span class="abs nav" style="left:887px">INTERIOR</span>
<span class="abs nav" style="left:986px">CONTACT US</span>

</body>
</html>
```